Flyer Vacation Gift Certificate

I need to create a beautiful flyer 8.5 x 11 PDF format flyer design. <br/><br/>Instructions:<br/>The flyer will really be a gift voucher for a las vegas vacation getaway. So must have a Las Vegas Theme exciting fun<br/><br/>The voucher should have two modules that will be editable. <br/>Must have a "Compliments Of" area and also must have an "Exclusively For" area<br/><br/>Keep in mind that this flyer will be printed so keep that in mind :)<br/><br/>Here the is the content for the vacation voucher:<br/><br/>There is no doubt that Las Vegas is one of the hottest travel destinations around the world. In fact, some people would even go as far as<br/>saying that perhaps it is THE hottest place to visit. Enjoy up to 4 nights of resort/casino accommodations in exciting Las Vegas, NV. Millions of people travel to this exciting city each year to enjoy its thrills. Thanks to the business you received this certificate from, now you can enjoy exciting Las Vegas, NV too!<br/><br/>Features:<br/>*Travel 7 Days A Week<br/>*Stay Your Choice Of Nights (1-4 Nights)<br/>*Good For Two Adults & Two Children<br/>*Pay Just The Taxes & Fees<br/>*Multiple Travel Date Requests Allowed<br/>*Fully Transferable To Another Person<br/>*Just A 30 Days Advance Notice Required<br/>*You Will Have 12 Months To Complete Travel After Redemption<br/><br/>HOW CAN WE DO THIS?<br/><br/>We contract with the world leading hotel chains and resorts to help them fill their otherwise empty rooms.<br/><br/>We help fill empty rooms which the hotels, resorts and cruise lines turn into additional revenue from other areas of their property and future bookings.<br/><br/>Hotels rarely experience full occupancy, yet they remain open, providing rooms and services at fixed costs. So when hotels give out their rooms by partnering with marketing companies like us, they might miss out on the room fee, but they already didn't have that in the first place, at least now they have the opportunity to gain a customer for their in-house restaurants, room service, their casinos, an extra day stay, future bookings, etc.<br/><br/>VIEW ALL THE DETAILS OF THIS SPECIAL OFFER AND REDEEM ONLINE AT <br/>WWW.TOPAZVOUCHERDESK.COM<br/><br/>Certificate ID # 47261-38504<br/>Expires 02/29/2020<br/><br/><br/>*terms and conditions apply see website for details<br/><br/>KEEP IN MIND THE EXAMPLES I AM UPLOADING ARE SIMPLY TO SHOW YOU THAT THEY CONTAIN THE "COMPLIMENTS OF" AND "EXCLUSIVELY FOR" ELEMENTS. THESE MUST BE INCLUDED IN NEW DESIGN. PLEASE ONLY USE THE CONTENT I PROVIDED IN BRIEF, DONT USE CONTENT FROM EXAMPLES.

Target Market(s)

CONSUMERS THAT HAVE BEEN REWARDED WITH A VACATION CERTIFICATE FOR DOING BUSINESS WITH A COMPANY.

COMPANIES USE THESE AS MARKETING INCENTIVES TO ATTRACT MORE CUSTOMERS AND TO REWARD LOYALTY, ETC.

Industry/Entity Type

Travel Industry

Colors

Designer to choose colors to be used in the design.

Requirements
Must have
• I need to create a beautiful flyer 8.5 x 11 PDF format flyer design.
• Instructions:
• The flyer will really be a gift voucher for a las vegas vacation getaway. So must have a Las Vegas Theme exciting fun
• The voucher should have two modules that will be editable.
• Must have a "Compliments Of" area and also must have an "Exclusively For" area
• Keep in mind that this flyer will be printed so keep that in mind :)
• Here the is the content for the vacation voucher:
• There is no doubt that Las Vegas is one of the hottest travel destinations around the world. In fact, some people would even go as far as
• saying that perhaps it is THE hottest place to visit. Enjoy up to 4 nights of resort/casino accommodations in exciting Las Vegas, NV. Millions of people travel to this exciting city each year to enjoy its thrills. Thanks to the business you received this certificate from, now you can enjoy exciting Las Vegas, NV too!
• Features:
• *Travel 7 Days A Week
• *Stay Your Choice Of Nights (1-4 Nights)
• *Good For Two Adults & Two Children
• *Pay Just The Taxes & Fees
• *Multiple Travel Date Requests Allowed
• *Fully Transferable To Another Person
• *Just A 30 Days Advance Notice Required
• *You Will Have 12 Months To Complete Travel After Redemption
• HOW CAN WE DO THIS?
• We contract with the world leading hotel chains and resorts to help them fill their otherwise empty rooms.
• We help fill empty rooms which the hotels, resorts and cruise lines turn into additional revenue from other areas of their property and future bookings.
• Hotels rarely experience full occupancy, yet they remain open, providing rooms and services at fixed costs. So when hotels give out their rooms by partnering with marketing companies like us, they might miss out on the room fee, but they already didn't have that in the first place, at least now they have the opportunity to gain a customer for their in-house restaurants, room service, their casinos, an extra day stay, future bookings, etc.
• VIEW ALL THE DETAILS OF THIS SPECIAL OFFER AND REDEEM ONLINE AT
• WWW.TOPAZVOUCHERDESK.COM
• Certificate ID # 47261-38504
• Expires 02/29/2020
• *terms and conditions apply see website for details
• KEEP IN MIND THE EXAMPLES I AM UPLOADING ARE SIMPLY TO SHOW YOU THAT THEY CONTAIN THE "COMPLIMENTS OF" AND "EXCLUSIVELY FOR" ELEMENTS. THESE MUST BE INCLUDED IN NEW DESIGN. PLEASE ONLY USE THE CONTENT I PROVIDED IN BRIEF, DONT USE CONTENT FROM EXAMPLES.
Nice to have
• EXCITING LAS VEGAS IMAGES THAT MAKE SOMEONE WANT TO GO THERE

```html
<!DOCTYPE html>
<html lang="en">
<head>
<meta charset="utf-8">
<title>Las Vegas Vacation Gift Certificate</title>
<link href="https://fonts.googleapis.com/css2?family=Montserrat:ital,wght@0,500;0,600;0,700;0,900;1,900&display=swap" rel="stylesheet">
<style>
:root{
  --ink-blue:#3a17f5;
  --cyan:#45f2de;
  --night:#07061a;
  --violet:#4a00a8;
  --magenta:#e21fe8;
  --white:#ffffff;
  --feature-line:#b23de0;
}
*{margin:0;padding:0;box-sizing:border-box}
html,body{width:927px;height:1200px;overflow:hidden;background:#fff}
.certificate{position:relative;width:927px;height:1200px;overflow:hidden;background:#fff;font-family:"Montserrat",sans-serif}

.night-panel{position:absolute;inset:0;width:927px;height:1200px}

.band{position:absolute;left:0;background:linear-gradient(90deg,var(--ink-blue) 0%,#3d8bec 55%,var(--cyan) 100%)}
.band-recipient{top:26px;height:57px;width:593px;clip-path:polygon(0 0,100% 0,97% 100%,0 100%)}
.band-recipient span{position:absolute;left:51px;top:12px;font-size:26px;font-weight:600;color:var(--white);letter-spacing:1px;white-space:nowrap}
.band-question{top:420px;height:93px;width:482px;clip-path:polygon(0 0,100% 0,96% 100%,0 100%)}
.band-question h2{position:absolute;left:52px;top:8px;font-size:39px;line-height:37px;font-weight:900;color:var(--white);letter-spacing:.5px}

.copy{position:absolute;left:52px;font-size:18.6px;line-height:27.2px;font-weight:500;white-space:nowrap;
  background:linear-gradient(100deg,var(--ink-blue) 0%,#3d70ee 45%,var(--cyan) 100%);
  -webkit-background-clip:text;background-clip:text;color:transparent}
.copy-intro{top:103px}
.copy-how{top:527px}

.compliments{position:absolute;left:600px;top:74px;width:296px;text-align:center;color:var(--white)}
.compliments p{font-size:24px;line-height:28px;font-weight:500;letter-spacing:.3px;white-space:nowrap}
.compliments .sender{margin:10px auto 0;width:288px;border:3px solid var(--white);padding:5px 0 4px;font-size:14px;font-weight:700;letter-spacing:.8px;white-space:nowrap}

.features-title{position:absolute;left:506px;top:220px;width:383px;height:56px;
  background:linear-gradient(160deg,var(--cyan) 0%,#3f8cee 45%,var(--ink-blue) 100%);
  clip-path:polygon(4% 0,100% 0,100% 100%,0 100%)}
.features-title span{position:absolute;left:50px;top:3px;font-size:46px;font-weight:900;font-style:italic;color:var(--white);letter-spacing:7px}

.feature{position:absolute;color:var(--white);font-size:24px;line-height:34px;font-weight:900;font-style:italic;white-space:nowrap}
.dot{position:absolute;width:19px;height:19px;border-radius:50%;background:linear-gradient(135deg,var(--cyan),#9a5cf0 45%,var(--magenta))}
.rule{position:absolute;height:3px;border-radius:2px;background:linear-gradient(90deg,var(--feature-line),var(--magenta) 60%,rgba(226,31,232,0))}

.skyline{position:absolute;left:575px;top:900px;width:352px;height:143px;
  background:linear-gradient(180deg,rgba(120,20,200,0) 0%,#a01ee0 40%,#e85ac8 80%,#f2c6f0 100%);
  clip-path:polygon(0 40%,40% 15%,70% 0,100% 10%,100% 100%,8% 100%)}

.footer{position:absolute;left:0;top:1043px;width:927px;height:157px;z-index:2;
  background:linear-gradient(180deg,var(--cyan) 0%,#3fa6ea 45%,var(--ink-blue) 100%);text-align:center;color:var(--white)}
.footer .cta{position:absolute;left:0;right:0;top:29px;font-size:18.3px;font-weight:600;letter-spacing:.2px;white-space:nowrap}
.footer .site{position:absolute;left:303px;top:54px;width:321px;height:25px;background:var(--white);border-radius:13px;
  color:#3a4af0;font-size:18px;font-weight:600;letter-spacing:2px;line-height:25px;white-space:nowrap}
.footer .meta{position:absolute;left:0;right:0;top:84px;font-size:18px;font-weight:600}
.footer .terms{position:absolute;left:0;right:0;top:112px;font-size:13.5px;font-weight:600}
.landmark{position:absolute;background:linear-gradient(180deg,rgba(255,255,255,.25),rgba(255,255,255,.08))}
.landmark-left{left:0;top:15px;width:95px;height:142px}
.landmark-right{left:818px;top:15px;width:109px;height:142px}
</style>
</head>
<body>
<main class="certificate">

  <svg class="night-panel" viewBox="0 0 927 1200" aria-hidden="true">
    <defs>
      <linearGradient id="nightSky" x1="0" y1="0" x2="0" y2="1">
        <stop offset="0" stop-color="#05050f"/>
        <stop offset="0.35" stop-color="#1b0a48"/>
        <stop offset="0.7" stop-color="#4400a6"/>
        <stop offset="1" stop-color="#8a10d8"/>
      </linearGradient>
    </defs>
    <polygon points="601,0 927,0 927,1043 560,1043 434,585 541,220" fill="url(#nightSky)"/>
    <circle cx="842" cy="376" r="2" fill="#f5c842"/>
    <circle cx="877" cy="420" r="1.6" fill="#e21fe8"/>
    <circle cx="848" cy="571" r="2" fill="#f5c842"/>
    <circle cx="885" cy="579" r="1.6" fill="#e21fe8"/>
    <circle cx="838" cy="593" r="1.6" fill="#e21fe8"/>
    <circle cx="866" cy="609" r="1.4" fill="#f5c842"/>
    <circle cx="890" cy="645" r="1.4" fill="#f5c842"/>
  </svg>

  <div class="skyline" role="img" aria-label="Illustration of a jet airliner taking off in front of the neon Las Vegas skyline"></div>

  <div class="band band-recipient"><span>Exclusively For : Customer Name</span></div>

  <p class="copy copy-intro">There is no doubt that Las Vegas is one of the<br>hottest travel destinations around the world.<br>In fact, some people would even go as far as<br>saying that perhaps it is THE hottest place to<br>visit. Enjoy up to 4 nights of resort/casino<br>accommodations in exciting Las Vegas, NV.<br>Millions of people travel to this exciting city<br>each year to enjoy its thrills.<br>Thanks to the business you received this<br>certificate from, now you can enjoy<br>exciting Las Vegas, NV too !</p>

  <div class="band band-question"><h2>HOW CAN<br>WE DO THIS ?</h2></div>

  <p class="copy copy-how">We contract with the world leading<br>hotel chains and resorts to help them<br>fill their otherwise empty rooms.<br>We help fill empty rooms which<br>the hotels, resorts and cruise lines turn<br>into additional revenue from other<br>areas of their property and future<br>bookings. Hotels rarely experience full<br>occupancy, yet they remain open,<br>providing rooms and services at fixed costs.<br>So when hotels give out their rooms by<br>partnering with marketing companies like us,<br>they might miss out on the room fee, but<br>they already didn't have that in the first place,<br>at least now they have the &nbsp;opportunity to<br>gain a customer for their in-house<br>restaurants, room service, their casinos, an<br>extra day stay, future bookings, etc.</p>

  <div class="compliments">
    <p>THIS CERTIFICATE IS<br>COMPLIMENTS OF</p>
    <div class="sender">WWW.TOPAZVOUCHERDESK.COM</div>
  </div>

  <div class="features-title"><span>FEATURES</span></div>

  <span class="dot" style="left:523px;top:304px"></span>
  <p class="feature" style="left:548px;top:296px">TRAVEL 7 DAYS A WEEK</p>
  <span class="rule" style="left:549px;top:329px;width:225px"></span>

  <span class="dot" style="left:510px;top:346px"></span>
  <p class="feature" style="left:536px;top:337px">&nbsp;STAY YOUR CHOICE OF<br>NIGHTS (1-4 NIGHTS)</p>
  <span class="rule" style="left:534px;top:409px;width:225px"></span>

  <span class="dot" style="left:485px;top:421px"></span>
  <p class="feature" style="left:510px;top:413px">&nbsp;GOOD FOR TWO ADULTS<br>&amp; TWO CHILDREN</p>
  <span class="rule" style="left:509px;top:483px;width:225px"></span>

  <span class="dot" style="left:465px;top:504px"></span>
  <p class="feature" style="left:491px;top:496px">PAY JUST THE TAXES &amp; FEES</p>
  <span class="rule" style="left:486px;top:532px;width:225px"></span>

  <span class="dot" style="left:455px;top:550px"></span>
  <p class="feature" style="left:482px;top:542px">MULTIPLE TRAVEL DATE<br>&nbsp;REQUESTS ALLOWED</p>
  <span class="rule" style="left:489px;top:611px;width:225px"></span>

  <span class="dot" style="left:471px;top:629px"></span>
  <p class="feature" style="left:496px;top:621px">FULLY TRANSFERABLE TO<br>&nbsp;ANOTHER PERSON</p>
  <span class="rule" style="left:504px;top:690px;width:225px"></span>

  <span class="dot" style="left:493px;top:711px"></span>
  <p class="feature" style="left:514px;top:703px">JUST A 30 DAYS ADVANCE<br>&nbsp;NOTICE REQUIRED</p>
  <span class="rule" style="left:534px;top:776px;width:225px"></span>

  <span class="dot" style="left:516px;top:790px"></span>
  <p class="feature" style="left:540px;top:782px">YOU WILL HAVE 12<br>&nbsp;&nbsp;&nbsp;&nbsp;MONTHS TO COMPLETE<br>&nbsp;&nbsp;&nbsp;&nbsp;&nbsp;TRAVEL AFTER<br>&nbsp;&nbsp;&nbsp;&nbsp;&nbsp;&nbsp;REDEMPTION</p>
  <span class="rule" style="left:580px;top:918px;width:225px"></span>

  <footer class="footer">
    <div class="landmark landmark-left" role="img" aria-label="Line drawing of a tower and globe"></div>
    <div class="landmark landmark-right" role="img" aria-label="Line drawing of a skyscraper and globe"></div>
    <p class="cta">VIEW ALL THE DETAILS OF THIS SPECIAL OFFER AND REDEEM ONLINE AT</p>
    <p class="site">www.topazvoucherdesk.com</p>
    <p class="meta">Certificate ID # 47261-38504 &nbsp;| &nbsp;Expires 02/29/2020</p>
    <p class="terms">*terms and conditions apply see website for details</p>
  </footer>

</main>
</body>
</html>
```